Kneadwell Bodycare

We are a Massage Therapy business based in Invercargill, New Zealand. We specialise in Sports and deep tissue massage but also provide relaxation and aromatherapy massage. We would like to see designs that use the the logo.
The final design should promote health and fitness.
Updates

Hi I am getting feedback that my business card picture is poor quality. I got this picture from plaza press under massage. So if you google this image a better quality picture should come up,. If not hope to upload a better image by tomorow, thanks.

Target Market(s)

Sports, people with pain and injuries

Industry/Entity Type

Massage

Requirements
Must have
• Logo, muscle body that is used on the business card, also a poster that matches my business card
Nice to have
• Picture of muscle man, shown on my business card
Should not have
• Not a picture of a real person

```html
<!DOCTYPE html>
<html lang="en">
<head>
<meta charset="utf-8">
<title>Kneadwell Bodycare Poster</title>
<link href="https://fonts.googleapis.com/css2?family=Roboto:wght@400;500;700;900&display=swap" rel="stylesheet">
<style>
  :root {
    --teal: #3aaec2;
    --teal-mid: #2a8fa3;
    --teal-dark: #1d6f80;
    --teal-light: #8fd3df;
    --ink: #111111;
    --paper: #ffffff;
    --price-light: #a8a8a8;
    --price-mid: #7b7b7b;
    --price-dark: #4d4d4d;
    --figure-light: #d9d9d9;
    --figure-dark: #7a7a7a;
  }
  * { margin: 0; padding: 0; box-sizing: border-box; }
  html, body { width: 849px; height: 1200px; overflow: hidden; background: var(--paper); }
  body { font-family: "Roboto", Arial, sans-serif; color: var(--ink); }
  .poster { position: relative; width: 849px; height: 1200px; overflow: hidden; background: var(--paper); }

  .brand { position: absolute; top: 30px; right: 28px; display: flex; align-items: center; gap: 22px; }
  .brand-name { font-size: 25px; font-weight: 500; color: var(--teal); }
  .brand-circle { width: 92px; height: 92px; border-radius: 50%; border: 6px solid var(--teal); }

  .anatomy-figure {
    position: absolute; left: 70px; top: 40px; width: 320px; height: 1120px;
    border-radius: 160px 160px 60px 60px;
    background: linear-gradient(180deg, var(--figure-light) 0%, var(--figure-dark) 55%, var(--figure-light) 100%);
  }

  .accents { position: absolute; inset: 0; pointer-events: none; }

  .headline { position: absolute; left: 425px; top: 222px; font-size: 52px; font-weight: 700; letter-spacing: -0.5px; }

  .services { position: absolute; left: 476px; top: 405px; list-style: none; }
  .services li { font-size: 28px; line-height: 57px; }

  .prices-title { position: absolute; left: 425px; top: 748px; font-size: 34px; }
  .price { position: absolute; top: 810px; width: 108px; text-align: center; }
  .price-disc { width: 108px; height: 108px; border-radius: 50%; display: flex; align-items: center; justify-content: center; color: var(--paper); font-size: 30px; }
  .price-time { margin-top: 22px; font-size: 16px; letter-spacing: 0.3px; }
  .price--30 { left: 419px; } .price--30 .price-disc { background: var(--price-light); }
  .price--60 { left: 569px; } .price--60 .price-disc { background: var(--price-mid); }
  .price--90 { left: 719px; } .price--90 .price-disc { background: var(--price-dark); }

  .phone { position: absolute; left: 44px; top: 1018px; display: flex; align-items: center; gap: 20px; font-size: 28px; }

  .footer-band {
    position: absolute; left: 0; bottom: 0; width: 100%; height: 110px; background: var(--teal);
    display: flex; align-items: center; padding-left: 58px; color: var(--paper); font-size: 19px;
  }
  .footer-band .address { margin-right: 18px; }
</style>
</head>
<body>
<main class="poster">
  <div class="anatomy-figure" role="img" aria-label="Illustration of a muscular human figure seen from behind, showing the anatomy of the back and legs"></div>

  <svg class="accents" width="849" height="1200" viewBox="0 0 849 1200" aria-hidden="true">
    <circle cx="318" cy="270" r="44" fill="var(--teal)" opacity="0.55"/>
    <circle cx="136" cy="452" r="34" fill="var(--teal)" opacity="0.45"/>
    <circle cx="340" cy="522" r="28" fill="var(--teal)" opacity="0.45"/>
    <circle cx="156" cy="792" r="44" fill="var(--teal)" opacity="0.5"/>
    <polygon points="610,420 820,380 849,560 700,600" fill="var(--teal-light)" opacity="0.55"/>
    <polygon points="560,600 800,470 849,700 690,720" fill="var(--teal-light)" opacity="0.7"/>
    <polygon points="700,520 849,460 849,760 760,780" fill="var(--teal)" opacity="0.75"/>
    <polygon points="780,560 849,540 849,800 800,740" fill="var(--teal-mid)"/>
    <polygon points="820,600 849,590 849,720" fill="var(--teal-dark)"/>
  </svg>

  <header class="brand">
    <span class="brand-name">Kneadwell Bodycare</span>
    <span class="brand-circle"></span>
  </header>

  <h1 class="headline">Are you in pain?</h1>

  <ul class="services">
    <li>Deep Tissue</li>
    <li>Sports Massage</li>
    <li>Relaxation</li>
    <li>Aromatherapy</li>
    <li>Hot Stones</li>
  </ul>

  <h2 class="prices-title">Prices</h2>
  <div class="price price--30"><div class="price-disc">$40</div><div class="price-time">30MINUTES</div></div>
  <div class="price price--60"><div class="price-disc">$60</div><div class="price-time">60MINUTES</div></div>
  <div class="price price--90"><div class="price-disc">$80</div><div class="price-time">90MINUTES</div></div>

  <div class="phone">
    <svg width="44" height="44" viewBox="0 0 44 44" aria-hidden="true">
      <circle cx="22" cy="22" r="20" fill="none" stroke="var(--ink)" stroke-width="2.5"/>
      <path d="M15 12c1.5-1 3-.5 3.5.5l2 4c.4.9 0 1.8-.8 2.3l-1.5 1c1 2.3 2.8 4.1 5.1 5.1l1-1.5c.5-.8 1.4-1.2 2.3-.8l4 2c1 .5 1.5 2 .5 3.5-1.2 1.8-3.2 2.6-5.2 2-6-1.8-10.7-6.5-12.5-12.5-.6-2 .2-4 1.6-5.6z" fill="var(--ink)"/>
    </svg>
    <span>0274815062</span>
  </div>

  <footer class="footer-band">
    <span class="address">18 Harbour Lane, Invercargill 9810</span>
    <span class="therapist">Mara Ellison Bachelor Therapeutic &amp; Sports massage</span>
  </footer>
</main>
</body>
</html>
```